Presentation card Launchpad KOVA - Tech Incubator from Perú

We need a Design to promote the incubator of technology Startups.
We are in Perú, we work with a string tech filter and develop enterprenurship competencies in the Startup team.
The card is to facilitators and staff memebers of LaunchpadKOVA.
We want a clear, modern, tech and agile Design.

We work to help New enterprises of technology here in Perú, we expect the candidates have a big competencies to Research and develop technological products.

We work using methodologies from QRB, Felstrom, Bellcourt and London univeesities. Our book base is The arte of the venturer.

We work events all year using diferent formats: Gridvane, Marlow prize, OTRV Plan Challenge you can use these logros in your Design.

Set the name, role, email, cell phone number, address.

Example:
// Contact info section
Osvaldo Quintanar
Rapid Prototyping Center Manager
osvaldo.quintanar@kova.edu.pe
(511) 988 437 216

// Address info section
LaunchpadKOVA
Technology-based business incubator
Av. Los Cedrales 475, Surquillo
Lima - Perú
web: launchpad-kova.org.pe
email: launchpad@kova.edu.pe
phone number: (511) 3692548 ext. 4186

// (optional)Lema section
Making happy using technology

// Social network section
facebook: launchpadkovaoficial

Target Market(s)

Enterprenurship, CTO, Investors, Companies interested on open innovation services

Industry/Entity Type

Information Technology

Contact Information for Business Card

Name, Role, Email, Cell phone number

Colors

Designer to choose colors to be used in the design.

Requirements
Must have
• Logo forms and colors
Nice to have
• I add pictures of the leaders of incubator
Should not have
• No vertical designs

```html
<!DOCTYPE html>
<html lang="en">
<head>
<meta charset="utf-8">
<title>Launchpad KOVA – Business Card</title>
<link rel="stylesheet" href="https://fonts.googleapis.com/css2?family=Nunito:wght@400;800;900&display=swap">
<style>
  :root {
    --crimson: #bc355a;
    --ink: #231f20;
    --paper: #ffffff;
    --backdrop: #ececec;
    --photo-dark: #2b3550;
    --photo-warm: #b9a48c;
  }
  * { box-sizing: border-box; margin: 0; padding: 0; }
  html, body { width: 1200px; height: 820px; overflow: hidden; }
  body {
    background: var(--backdrop);
    font-family: "Nunito", sans-serif;
    position: relative;
  }
  .card {
    position: absolute;
    top: 240px;
    width: 570px;
    height: 340px;
    background: var(--paper);
    overflow: hidden;
    box-shadow: 0 8px 22px rgba(0,0,0,0.15);
  }
  .card--front { left: 20px; }
  .card--back { left: 610px; }
  .card svg.card-shapes { position: absolute; inset: 0; }
  .abs { position: absolute; white-space: nowrap; }

  /* front */
  .tagline {
    left: 33px; top: 99px;
    font-weight: 800; font-size: 21px; line-height: 25px;
    color: var(--ink);
  }
  .tagline .accent { color: var(--crimson); }
  .address {
    left: 29px; top: 178px;
    color: var(--paper); font-size: 16px; line-height: 20px;
  }
  .contact-list {
    left: 29px; top: 222px;
    color: var(--paper); font-size: 15px; line-height: 22px;
    list-style: none;
  }
  .contact-list b { font-weight: 900; margin-right: 2px; }
  .social { display: flex; align-items: center; gap: 8px; margin-top: 2px; }
  .social-dot { width: 12px; height: 12px; border-radius: 50%; background: #3b5fa8; }
  .brand {
    font-weight: 900; letter-spacing: -0.5px;
  }
  .brand--front {
    left: 350px; top: 84px;
    font-size: 42px; line-height: 48px; color: var(--paper);
  }
  .brand--back {
    left: 111px; top: 54px;
    font-size: 30px; line-height: 34px; color: var(--ink);
  }

  /* back */
  .person {
    right: 18px; top: 200px; text-align: right;
  }
  .person-name { font-weight: 800; font-size: 25px; line-height: 28px; color: var(--ink); }
  .person-name .accent { color: var(--crimson); }
  .person-role { font-size: 16px; line-height: 20px; color: var(--crimson); }
  .person-contact {
    right: 193px; top: 271px; text-align: right;
    font-size: 15px; line-height: 23px; color: var(--ink);
  }
  .person-contact .phone { padding-right: 27px; display: block; }
  .motto {
    right: 21px; top: 273px; text-align: right;
    font-size: 15px; line-height: 18px; color: var(--paper);
  }
</style>
</head>
<body>

<section class="card card--front">
  <svg class="card-shapes" width="570" height="340" viewBox="0 0 570 340" aria-hidden="true">
    <path d="M0,84 C60,40 160,10 242,0 L570,0 L570,259 C500,310 420,330 332,340 L0,340 Z" fill="var(--crimson)"/>
    <path d="M0,93 L265,93 C250,110 242,135 239,162 L0,162 Z" fill="var(--paper)"/>
  </svg>
  <h2 class="abs tagline">Technology-based<br><span class="accent">business incubator</span></h2>
  <p class="abs address">Av. Los Cedrales 475, Surquillo<br>Lima - Perú</p>
  <ul class="abs contact-list">
    <li><b>e:</b>launchpad@kova.edu.pe</li>
    <li><b>w:</b> launchpad-kova.org.pe</li>
    <li><b>p:</b> (511) 3692548 ext. 4186</li>
    <li class="social"><span class="social-dot"></span>launchpadkovaoficial</li>
  </ul>
  <div class="abs brand brand--front">Launchpad<br>KOVA</div>
</section>

<section class="card card--back">
  <svg class="card-shapes" width="570" height="340" viewBox="0 0 570 340">
    <defs>
      <linearGradient id="photoTone" x1="0" y1="0" x2="1" y2="1">
        <stop offset="0" stop-color="var(--photo-warm)"/>
        <stop offset="0.45" stop-color="var(--photo-dark)"/>
        <stop offset="1" stop-color="#6d5a4a"/>
      </linearGradient>
    </defs>
    <path d="M0,0 L72,0 C88,30 95,60 90,82 C86,120 50,150 47,205 C45,260 90,310 112,340 L0,340 Z" fill="var(--crimson)" aria-hidden="true"/>
    <path role="img" aria-label="Group photo of the incubator team and leaders" d="M289,0 L570,0 L570,172 C520,185 440,172 385,125 C345,90 310,45 289,0 Z" fill="url(#photoTone)"/>
    <path d="M392,271 L570,271 L570,315 L355,315 C372,305 385,290 392,271 Z" fill="var(--crimson)" aria-hidden="true"/>
  </svg>
  <div class="abs brand brand--back">Launchpad<br>KOVA</div>
  <div class="abs person">
    <h1 class="person-name">Osvaldo <span class="accent">Quintanar</span></h1>
    <p class="person-role">Rapid Prototyping Center Manager</p>
  </div>
  <p class="abs person-contact">osvaldo.quintanar@kova.edu.pe<span class="phone">(511) 988 437 216</span></p>
  <p class="abs motto">Making happy<br>using technology</p>
</section>

</body>
</html>
```